Flyer for an online formula one racing league

Hello.

I am looking for the perfect one page facebook/instagram style flyer for an online formula one racing league. The racing league is called 'VOLTA RACING LEAGUE'.

Information that MUST be on the new flyer is already on the old flyer I have uploaded here. In addition to including: The Volta racing league 'V' logo I have uploaded AND the text: 'Very popular, clean and competitive racing league, running for its 4th season. Why not join with a friend? Race times, Mondays, Tuesdays and Wednesdays each at 8pm UK TIME Message below for any questions. (Spacing of information is not important, however all the information in regards to the racing I have just mentioned MUST BE on the flyer, this includes info from old pic, logo and the other info I just mentioned).

It would be beneficial to have lots of dark blue on the flyer and the new flyer to be a lot different to the original flyer I uploaded, but this is not essential.

I apologise if I did not explain very well, any questions, please message me.

The best flyer should look the most attractive to someone that might be interested in joining an online formula one racing league.

I used this website before to create the perfect logo for my Sunday League team last year, and I was very impressed. I look forward to seeing your submissions.

Target Market(s)

No specific target, more something that may attract someone into joining a formula one online racing league

Industry/Entity Type

e sports/formula one

Colors
0054AA
0677BA
7BADD7
CADEEF
E8F1F8

Requirements
Must have
• Read product description please
Should not have
• Ignoring product description!

```html
<!DOCTYPE html>
<html lang="en">
<head>
<meta charset="utf-8">
<title>Volta Racing League</title>
<link href="https://fonts.googleapis.com/css2?family=Russo+One&display=swap" rel="stylesheet">
<style>
  :root {
    --navy: #0b1a45;
    --navy-deep: #060f2a;
    --royal: #0054aa;
    --cerulean: #0677ba;
    --sky: #7badd7;
    --ice: #e8f1f8;
    --teal: #2c8aa0;
    --ember: #e0572a;
    --ember-deep: #7a1d12;
    --silver-top: #f4f4f4;
    --silver-bottom: #9a9a9a;
    --text-light: #e8f1f8;
    --shadow: rgba(0, 0, 0, 0.85);
  }
  html, body {
    margin: 0;
    padding: 0;
    width: 1200px;
    height: 628px;
    overflow: hidden;
    background: var(--navy-deep);
  }
  .flyer {
    position: relative;
    width: 1200px;
    height: 628px;
    overflow: hidden;
    font-family: "Russo One", "Arial Black", sans-serif;
    text-transform: uppercase;
    text-align: center;
    color: var(--text-light);
  }
  .race-scene {
    position: absolute;
    inset: 0;
    background:
      radial-gradient(ellipse 42% 55% at 50% 48%, rgba(6, 15, 42, 0.6), transparent 70%),
      radial-gradient(ellipse 40% 55% at 92% 22%, rgba(240, 110, 40, 0.7), transparent 70%),
      radial-gradient(ellipse 45% 60% at 8% 25%, rgba(6, 119, 186, 0.75), transparent 70%),
      linear-gradient(90deg, var(--royal) 0%, var(--cerulean) 16%, var(--navy) 42%, #1e1d3a 62%, var(--ember) 88%, var(--ember-deep) 100%);
  }
  .race-scene::after {
    content: "";
    position: absolute;
    inset: 0;
    background: linear-gradient(180deg, rgba(6,15,42,0.2) 0%, rgba(6,15,42,0) 38%, rgba(6,15,42,0.75) 100%);
  }
  .line {
    position: absolute;
    left: 0;
    right: 0;
    margin: 0;
    white-space: nowrap;
    text-shadow: 3px 3px 4px var(--shadow), 0 0 10px var(--shadow);
  }
  .title {
    top: 30px;
    font-size: 78px;
    letter-spacing: 4px;
    line-height: 1;
    background: linear-gradient(180deg, var(--silver-top) 0%, #d0d0d0 45%, var(--silver-bottom) 100%);
    -webkit-background-clip: text;
    background-clip: text;
    -webkit-text-fill-color: transparent;
    filter: drop-shadow(3px 4px 2px var(--shadow));
    text-shadow: none;
  }
  .tagline {
    top: 146px;
    font-size: 30px;
    line-height: 34px;
    letter-spacing: 1.5px;
    color: #d4d8de;
  }
  .season {
    top: 296px;
    font-size: 41px;
    line-height: 42px;
    letter-spacing: 1.5px;
  }
  .divisions {
    top: 444px;
    font-size: 35px;
    line-height: 44px;
    letter-spacing: 1px;
  }
  .race-times {
    top: 562px;
    font-size: 27px;
    line-height: 30px;
    letter-spacing: 0.5px;
    color: #d6dde6;
  }
  .message {
    top: 597px;
    font-size: 17px;
    line-height: 22px;
    letter-spacing: 1px;
    color: var(--sky);
  }
  .badge {
    position: absolute;
    top: 266px;
    width: 132px;
    height: 132px;
    border-radius: 50%;
    background: var(--navy);
    display: flex;
    align-items: center;
    justify-content: center;
    font-size: 22px;
    letter-spacing: 1px;
    color: var(--ice);
  }
  .badge--left { left: 58px; }
  .badge--right { left: 996px; }
</style>
</head>
<body>
  <main class="flyer">
    <div class="race-scene" role="img" aria-label="Formula one cars racing at speed with blue and orange light streaks"></div>

    <h1 class="line title">Volta Racing League</h1>
    <p class="line tagline">Very popular, clean and competitive racing league</p>

    <div class="badge badge--left">Volta</div>
    <div class="badge badge--right">Volta</div>

    <p class="line season">Running for its 4th season.<br>Why not join with a friend?</p>
    <p class="line divisions">Clean online racing league<br>3 divisions currently and looking to keep growing!</p>
    <p class="line race-times">Race times: Mondays, Tuesdays and Wednesdays each at 8pm UK time</p>
    <p class="line message">Message below for any questions</p>
  </main>
</body>
</html>
```